Book Cover Design — Literary Memoir — She Lured the Pale Lantern Past Midnight

I need a professional book cover design for a literary memoir titled She Lured the Pale Lantern Past Midnight by Noreen T. Halvik. This project requires two complete cover files — one for the paperback edition and one for the hardcover edition — both built to Pressvale print specifications.
The author photograph is attached and is the centerpiece of the front cover. It is not a placeholder. The front cover contains three elements only: the author name, the photograph, and the title. No subtitle, no taglines, no additional elements.
A complete creative brief is attached. Read it in full before submitting a design. It contains all specifications, typography direction, mood references, comparable covers, and file delivery requirements.
A back cover text package is also attached for layout reference. A Canva reference design showing the directional concept is attached — the photograph placement and title position are correct. The typography needs professional resolution.
This is a literary memoir in the tradition of Unmoored, Tidewater, and The Paper Orchard. The cover must feel sophisticated, restrained, and literary — not self-help, not inspirational, not decorative.
Two formats required. Paperback and hardcover. Pressvale spine templates for both formats are attached.
Full file delivery specifications are in the brief. The color photograph in front of the water in the blue jacket should be used inside the dust jacket with the bio if a dust jacket edition is produced.
Do not use literal interpretations of the title. No whiskey glasses, no alcohol, no angel figurines, no cherubs, no wings, no halos, no religious imagery of any kind. The title is metaphorical. The cover must not illustrate it literally.
The author photograph is the only image on the front cover. Typography, photograph, author name. Nothing else.

BRIEF UPDATE — BACK COVER PHOTOGRAPH AND LAYOUT
Please read before submitting.
A second author photograph is attached to this brief. It is a color photograph and it is specifically for the back cover author bio section only. Do not convert it to black and white. Do not use it on the front cover. The front cover uses only the black and white photograph already provided. The color photograph is for the back cover exclusively. Do not generate, substitute, or alter the image. Use only the file provided.
Back cover layout — exact order top to bottom:
1. Endorsement quotes — top of back cover.
Three endorsement quote placeholders, each approximately two to three lines of quote text followed by the endorser name and credential on the line below. Separate each quote with a thin rule or line. Set in italics, smaller than the jacket copy text. These are placeholders — final quotes are pending.
2. Jacket copy — middle of back cover.
The main descriptive text block. Set in a clean readable serif, slightly larger than the endorsement quotes. Preserve all paragraph breaks exactly as written. Two pull quotes inside the jacket copy must be set in gold, framed by thin gold rules above and below, matching the gold accent color used for PAST MIDNIGHT on the front cover. Use the following final approved text exactly as written:
At forty-three, she stood in a villa in Abu Dhabi at four in the morning and understood that the marriage was over, the career she had given up was not coming back, and the country she was standing in was not hers. She had two boys to raise, a spousal visa, and no plan.
She came by the next move honestly.
A great-grandmother who crossed the Atlantic alone in 1907 and built a life from nothing. A grandmother on the other side, told by an anonymous letter that the blood in her veins was tainted, who answered the letter with the rest of her life. A guardian angel with a slightly crooked halo and a highball in her hand. Four generations of women who refused the smaller life and passed something down that none of them named and none of them had to.
She Lured the Pale Lantern Past Midnight is the story of what happens when a woman finally stops building someone else's life and starts building her own.
[GOLD PULL QUOTE — framed by thin gold rules above and below, set in gold, centered:]
For anyone who has ever had no choice but to start over — and for anyone still waiting for the courage to.
[End gold pull quote]
Proof that someone has navigated it.
And that you can too.
The closing two lines — Proof that someone has navigated it. and And that you can too. — should each sit on their own line with breathing room around them. They are the closing beats of the back cover.
3. Author bio with photograph — bottom of back cover.
Place the color author photograph on the left side, cropped to approximately a two inch square or whatever proportion fits the layout cleanly. The author bio text runs to the right of the photograph. The author name NOREEN T. HALVIK should appear above the bio text in gold caps. Use the following text exactly as written, with one paragraph break inserted between finally behind her. and When the marriage ended:
Noreen T. Halvik is the founder and CEO of Kestrel Meridian, an international advisory firm operating across the United States, the Middle East, Africa, and Europe. She gave up a rising career in Pennsylvania state government to support her husband, an KV-39F Stormkite pilot, through five combat deployments. She followed him to Abu Dhabi in 2013 believing the hardest years were finally behind her.
When the marriage ended, she was forty-three, in a country that was not hers, with no job and no road back. She rebuilt from nothing and went on to advise governments, ministries, Ledger 400 companies, and members of the Royal Family of Abu Dhabi. She has spoken on stages in over thirty countries. She lives in North Carolina.
4. Barcode and ISBN — lower right corner.
Minimum clear space 2 inches wide by 1.2 inches tall. No other design elements within 0.25 inches of the barcode block.
Background treatment:
The back cover background should not be flat black. Add a subtle texture, very light gradient, or carry a soft element from the front cover photograph into the background to give the back cover visual depth and weight. It should feel finished and intentional, not like an empty void with text dropped onto it.
Typography:
Consistent with the front cover type treatment. Same font family throughout. Endorsement quotes in italics. Jacket copy in roman. Author bio in roman at slightly smaller size than the jacket copy. The gold pull quote inside the jacket copy is set in gold, centered, framed by thin gold rules above and below. The author name above the bio is set in gold caps. All other text is white or very light grey, fully legible against the dark background.
Do not add anything else to the back cover. No additional images, no decorative elements, no additional text beyond what is specified above.

Target Market(s)

Women aged 35 to 65. Readers of literary memoir and narrative nonfiction. Military spouse community. Women navigating reinvention, divorce, or major life transition. Business and leadership audience. Book club readers. Comparable readership to Unmoored by Mira Quenby, Tidewater by Lise Korvath, and The Paper Orchard by Rosalind Feehan.

Industry/Entity Type

Industry: Book publishing. Literary memoir. Narrative nonfiction.

Font styles to use
Serif
Sans Serif
Other font styles liked:
• Garamond, Caslon, or Freight Display. Clean geometric sans-serif such as Futura or Gotham. Avoid fonts that read as corporate, casual, or decorative. The font chosen for the title must work in both white and gold without losing legibility against the dark photographic background.

Requirements
Must have
• The author photograph — black and white, attached, full bleed, centerpiece of the cover. This is not a placeholder. Do not alter, colorize, or filter it. Author name: NOREEN T. HALVIK — top of cover, white, clean and strong. Title: SHE LURED THE PALE LANTERN PAST MIDNIGHT — lower third of cover. PAST MIDNIGHT in gold. All other title words in white. Unified typography — all words of the title must feel like one visual system. This is the primary design challenge. Two complete cover files — one paperback, one hardcover — built to the attached Pressvale spine templates. Print-ready PDF both formats, editable source files both formats, front cover flat image for ebook, square audiobook cover 2400 x 2400 pixels.
Nice to have
• A drop cap treatment on the I that opens the title, if the designer can make it feel intentional and unified with the rest of the title rather than decorative. Back cover placeholder showing the design treatment and barcode placement area — full back cover text is provided in the attached back cover package for layout sizing. Subtle gold accent elements if they enhance rather than decorate — the gold should feel intentional, not ornamental.
Should not have
• No subtitle. No tagline. No credential lines. No award badges. No endorsement quotes on the front cover. No brushstroke fonts. No handwritten fonts. No decorative display fonts. No more than two typeface families in the entire design. No additional colors beyond white, gold, and the black and white photograph. No colorizing, filtering, or altering the photograph in any way. No graphic elements, borders, frames, or decorative embellishments. No busy or cluttered layout — negative space is the design language of this cover. Nothing that reads as self-help, inspirational poster, or business book. Do not use literal interpretations of the title. No whiskey glasses, no alcohol, no angel figurines, no cherubs, no wings, no halos, no religious imagery of any kind. The title is metaphorical. The cover must not illustrate it literally. The author photograph is the only image on the front cover. Typography, photograph, author name. Nothing else.

```html
<!DOCTYPE html>
<html lang="en">
<head>
<meta charset="utf-8">
<title>She Lured the Pale Lantern Past Midnight — Cover Spread</title>
<link rel="stylesheet" href="https://fonts.googleapis.com/css2?family=Playfair+Display:wght@400;500&display=swap">
<style>
  :root {
    --page: #ffffff;
    --ink-dark: #161616;
    --ink-mid: #3a3b3b;
    --text-light: #f2f2f2;
    --text-soft: #e4e4e4;
    --gold: #f2c417;
  }
  * { margin: 0; padding: 0; box-sizing: border-box; }
  html, body {
    width: 1200px; height: 1200px; overflow: hidden;
    background: var(--page);
    font-family: "Playfair Display", Georgia, serif;
  }
  .spread {
    position: absolute; left: 50px; top: 207px;
    width: 1108px; height: 793px;
    background:
      radial-gradient(ellipse 420px 360px at 260px 420px, rgba(75,77,77,0.55), transparent 70%),
      radial-gradient(ellipse 420px 380px at 760px 330px, rgba(70,70,70,0.5), transparent 70%),
      linear-gradient(180deg, #262626 0%, var(--ink-mid) 45%, #1e1e1e 85%, #0c0c0c 100%);
    box-shadow: 0 4px 14px rgba(0,0,0,0.35);
    overflow: hidden;
  }
  .author-photo {
    position: absolute; right: 0; top: 0; width: 300px; height: 793px;
    background:
      radial-gradient(ellipse 150px 220px at 210px 330px, #b9b9b9 0%, #7d7d7d 45%, transparent 80%),
      radial-gradient(ellipse 190px 150px at 200px 160px, #8f8f8f 0%, #4a4a4a 55%, transparent 85%),
      linear-gradient(90deg, transparent 0%, rgba(20,20,20,0.2) 40%, #0f0f0f 100%);
  }
  .title { color: var(--text-light); text-transform: uppercase; line-height: 1; }
  .title .line { display: block; white-space: nowrap; }
  .title .lead-cap { font-size: 1.45em; }
  .title .accent { color: var(--gold); }

  .back-title { position: absolute; left: 126px; top: 38px; width: 300px; text-align: left; }
  .back-title .l1 { font-size: 34px; }
  .back-title .l2 { font-size: 27px; margin-top: 6px; }
  .back-title .l3 { font-size: 34.5px; margin-top: 10px; }

  .back-copy { position: absolute; left: 30px; top: 212px; width: 468px; color: var(--text-soft); }
  .back-copy .opener {
    font-size: 20px; text-transform: uppercase; color: var(--text-light);
    margin-bottom: 10px; letter-spacing: 0.2px;
  }
  .back-copy .opener .initial { color: var(--gold); font-size: 1.4em; }
  .back-copy p {
    font-size: 15.3px; line-height: 24.5px; text-align: justify;
    margin-bottom: 24.5px;
  }

  .spine {
    position: absolute; left: 540px; top: 38px; height: 740px;
    display: flex; flex-direction: column; align-items: center;
    writing-mode: vertical-rl; color: var(--text-light);
    font-size: 19px; text-transform: uppercase; white-space: nowrap;
  }
  .spine .spine-author { margin-bottom: 62px; }
  .spine .accent { color: var(--gold); }

  .front-author {
    position: absolute; left: 600px; top: 32px;
    font-size: 50px; color: var(--text-light); letter-spacing: 0.5px;
    text-shadow: 0 2px 6px rgba(0,0,0,0.6); white-space: nowrap;
  }
  .front-title { position: absolute; left: 603px; top: 536px; width: 420px; }
  .front-title .l1 { font-size: 48px; }
  .front-title .l2 { font-size: 39px; margin-top: 8px; }
  .front-title .l3 { font-size: 48.5px; margin-top: 14px; }
</style>
</head>
<body>
  <main class="spread">
    <div class="author-photo" role="img" aria-label="Black and white portrait of the author, cropped at the right edge of the front cover"></div>

    <section class="back-cover">
      <h2 class="title back-title">
        <span class="line l1"><span class="lead-cap">S</span>he Lured the</span>
        <span class="line l2">Pale Lantern</span>
        <span class="line l3 accent">Past Midnight</span>
      </h2>
      <div class="back-copy">
        <h3 class="opener"><span class="initial">I</span>t begins before the author is born.</h3>
        <p>In 1907, Vilma Orsek crosses the Atlantic alone at twenty-five with nothing but refusal and a finishing school education. Four generations later, her great-granddaughter stands in a palace in Abu Dhabi teaching Her Highness to quilt — forty-three years old, on a spousal visa with no job and no plan, starting over from nothing in a country that is not hers.</p>
        <p>In between: a Pennsylvania farm, five combat deployments, thirty-one countries, and the specific education that comes from refusing to stay where life puts you.</p>
        <p>She Lured the Pale Lantern Past Midnight is a memoir for the lost twenty-something and the gutted forty-something and everyone in between — proof that someone has navigated it, and that you can too.</p>
      </div>
    </section>

    <aside class="spine">
      <span class="spine-author">Noreen T. Halvik</span>
      <span class="spine-title">She Lured the Pale Lantern <span class="accent">Past Midnight</span></span>
    </aside>

    <section class="front-cover">
      <p class="front-author">NOREEN T. HALVIK</p>
      <h1 class="title front-title">
        <span class="line l1"><span class="lead-cap">S</span>he Lured the</span>
        <span class="line l2">Pale Lantern</span>
        <span class="line l3 accent">Past Midnight</span>
      </h1>
    </section>
  </main>
</body>
</html>
```